Vice chair

I'm running for a position as vice chair this will be posted in the lunch room cafeteria in this package i posted logos, my picture, sample of old flyers to give you a idea i also wrote literature need help in putting it together like it to look like a million bucks goal win this election I summited lots of pdf files and jpeg look though them to help with your design feel free to contact me to further assist you
Updates

Would like this to be completed by Wednesday

Target Market(s)

My constituents

Font styles to use
Serif

Colors

Designer to choose colors to be used in the design.

Requirements
Must have
• Make it look clean neat
Nice to have
• Nice background

```html
<!DOCTYPE html>
<html lang="en">
<head>
<meta charset="utf-8">
<title>Vote Independent – Vice Chair</title>
<link href="https://fonts.googleapis.com/css2?family=Open+Sans:wght@400;600;700;800&display=swap" rel="stylesheet">
<style>
  :root {
    --navy: #0d2f8a;
    --blue-deep: #0a2a86;
    --blue-mid: #1f4fc4;
    --sky: #2fa3e6;
    --red: #c8242e;
    --red-deep: #a81c25;
    --ink: #2a2a2a;
    --paper: #ffffff;
    --grey: #d9dadc;
    --green: #2e8b2e;
    --gold: #c9922a;
    --bg: #eeeeee;
  }
  * { margin: 0; padding: 0; box-sizing: border-box; }
  html, body { width: 707px; height: 1200px; overflow: hidden; background: var(--bg); }
  body { font-family: "Open Sans", Arial, sans-serif; color: var(--ink); }

  .flyer {
    position: relative; width: 707px; height: 1200px; overflow: hidden;
    background: linear-gradient(180deg, var(--paper) 0%, var(--paper) 68%, var(--grey) 100%);
  }
  .header-band {
    position: absolute; left: 0; top: 0; width: 707px; height: 300px;
    background: radial-gradient(ellipse at 65% 30%, var(--blue-mid) 0%, var(--blue-deep) 70%);
  }
  .ribbon { position: absolute; left: 0; width: 707px; }
  .ribbon-top { top: 190px; height: 150px; }
  .ribbon-bottom { top: 740px; height: 140px; }

  .portrait {
    position: absolute; left: 0; top: 40px; width: 262px; height: 490px;
    background: linear-gradient(180deg, #b08a72 0%, #8a6a58 45%, #1e1e1e 72%, #111 100%);
    border-radius: 0 120px 0 0;
  }

  .depots { position: absolute; top: 58px; left: 308px; display: flex; gap: 22px; }
  .depot { width: 104px; text-align: center; }
  .depot-mark {
    width: 100px; height: 100px; border-radius: 50%;
    background: #f2f2f2; border: 3px solid #fff; margin: 0 auto 6px;
  }
  .depot-name { color: #fff; font-weight: 700; font-size: 12px; letter-spacing: .5px; }

  .headline { position: absolute; right: 36px; top: 352px; text-align: right; }
  .headline-vote {
    font-weight: 800; font-size: 136px; line-height: 1; letter-spacing: -3px;
    color: var(--red);
    background: linear-gradient(180deg, #e23a44 0%, var(--red-deep) 100%);
    -webkit-background-clip: text; background-clip: text; -webkit-text-fill-color: transparent;
  }
  .headline-sub {
    font-weight: 700; font-size: 30px; color: var(--navy); letter-spacing: .5px; margin-top: -4px;
  }

  .intro { position: absolute; top: 552px; left: 32px; right: 34px; display: flex; gap: 36px; }
  .intro p { flex: 1; font-size: 13.6px; line-height: 1.45; text-align: justify; }

  .credentials { position: absolute; top: 888px; left: 36px; width: 390px; list-style: none; font-size: 11.6px; line-height: 1.5; }
  .credentials li { position: relative; padding-left: 20px; margin-bottom: 12px; }
  .credentials li::before {
    content: ""; position: absolute; left: 2px; top: 6px; width: 6px; height: 6px; border-radius: 50%; background: var(--navy);
  }
  .credentials .sign-off { padding-left: 20px; }
  .credentials .sign-off::before { display: none; }

  .slate { position: absolute; left: 448px; top: 862px; width: 230px; text-align: center; }
  .slate-text {
    font-weight: 800; font-size: 32px; color: var(--blue-mid); transform: rotate(6deg); display: inline-block;
  }
  .slate-box {
    display: inline-block; margin-top: 2px; width: 40px; height: 40px; border: 2px solid var(--navy);
    font-weight: 800; font-size: 34px; line-height: 36px; color: var(--blue-mid);
  }

  .union { position: absolute; left: 440px; top: 1020px; width: 240px; display: flex; align-items: center; gap: 10px; }
  .union-mark { width: 96px; height: 96px; border-radius: 50%; background: var(--gold); flex: none; }
  .union-name { font-weight: 800; font-size: 22px; line-height: 1.1; color: var(--green); }
</style>
</head>
<body>
<main class="flyer">
  <div class="header-band"></div>

  <svg class="ribbon ribbon-top" viewBox="0 0 707 150" preserveAspectRatio="none" aria-hidden="true">
    <path d="M0 70 C180 40 330 105 707 40 L707 150 L0 150 Z" fill="#ffffff"/>
    <path d="M0 70 C180 40 330 105 707 40 L707 62 C330 127 180 62 0 92 Z" fill="#1f4fc4"/>
    <path d="M0 92 C180 62 330 127 707 62 L707 76 C330 141 180 76 0 106 Z" fill="#ffffff"/>
    <path d="M0 106 C180 76 330 141 707 76 L707 90 C330 155 180 90 0 120 Z" fill="#c8242e"/>
    <path d="M0 120 C180 90 330 155 707 90 L707 150 L0 150 Z" fill="#ffffff"/>
  </svg>

  <div class="portrait" role="img" aria-label="Portrait photo of the candidate"></div>

  <div class="depots">
    <div class="depot"><div class="depot-mark"></div><div class="depot-name">North Yard</div></div>
    <div class="depot"><div class="depot-mark"></div><div class="depot-name">Ridge Yard</div></div>
    <div class="depot"><div class="depot-mark"></div><div class="depot-name">Hill Yard</div></div>
  </div>

  <div class="headline">
    <div class="headline-vote">VOTE</div>
    <div class="headline-sub">INDEPENDENT [X]</div>
  </div>

  <section class="intro">
    <p>I Marcus Rivera for those who don't know me would like to introduce myself I have always been approachable and helpful whether you are a probationary officer or a veteran operator with knowledge or information. We must protect our union rules for ourselves our future and most important our children.</p>
    <p>I would like this opportunity to run as your vice chair a person you can trust and believe in me Positive and motivations are my main keys for progress and for change in my campaign When there are no leaders to lookup to one therefore must become one I do believe I'm the right person for this position so please come out and support me and vote me as your vice chair</p>
  </section>

  <svg class="ribbon ribbon-bottom" viewBox="0 0 707 140" preserveAspectRatio="none" aria-hidden="true">
    <path d="M0 40 C200 30 300 80 420 70 C520 60 600 20 707 25 L707 50 C600 45 520 85 420 95 C300 105 200 55 0 65 Z" fill="#1f4fc4"/>
    <path d="M0 65 C200 55 300 105 420 95 C520 85 600 45 707 50 L707 60 C600 55 520 95 420 105 C300 115 200 65 0 75 Z" fill="#2fa3e6"/>
    <path d="M0 80 C200 70 300 118 420 110 C520 100 600 62 707 66 L707 76 C600 72 520 110 420 120 C300 128 200 80 0 90 Z" fill="#c8242e"/>
    <path d="M0 94 C200 84 300 130 420 122 C520 112 600 76 707 80 L707 88 C600 84 520 120 420 130 C300 138 200 92 0 102 Z" fill="#a81c25"/>
  </svg>

  <ul class="credentials">
    <li>20 years on the job</li>
    <li>Past union member of Carriers Guild local 310 believes in There is a collective bargaining agreement in place and no management is above the law to violate it</li>
    <li>Past union member of Carriers Guild local 742 believes a house that is divided cannot stand alone</li>
    <li>In closing I believe that our union does not stand out individually achievement we must stand for collective advancement for all. we must always continue to stand together, stay together &amp; fight together so we can win together because success is never owned, it is rented and the rent is due every day.</li>
    <li class="sign-off">Vote independent me as your vice chair</li>
  </ul>

  <div class="slate">
    <div class="slate-text">Vote the slate</div><br>
    <div class="slate-box">X</div>
  </div>

  <div class="union">
    <div class="union-mark"></div>
    <div class="union-name">Transit Crew Alliance</div>
  </div>
</main>
</body>
</html>
```